One Page PDF Educational Handout Design for Women and Students

We need a 1-2 page PDF created that outlines 11 steps in a process. The attached style guide contains information on how to design the document (page 1). Pages 2-3 need to be formatted in a visually appealing manner to call attention to the 11 steps and substeps.

We would like the design to include our logo, the title, the steps, and contain colors, sections and stimulating design.

Target Market(s)

College Students, Women 18-30 years old.

Industry/Entity Type

Education

Font styles to use
Sans Serif

Colors
33a6d7
f04a50
f68d4d

Requirements
Must have
• Colors, Logo, Titles, Organized by Title/Subtitle. 1-2 pages. Visually stimulating and appealing.

```html
<!DOCTYPE html>
<html lang="en">
<head>
<meta charset="utf-8">
<title>11 Nursing Test Taking Tips</title>
<link rel="stylesheet" href="https://fonts.googleapis.com/css2?family=Archivo+Black&family=Barlow:wght@400;600;700&family=Barlow+Semi+Condensed:wght@600;700&display=swap">
<style>
  :root {
    --coral: #ef5f5a;
    --blue-band: #5c8fbe;
    --blue-text: #2c56a3;
    --dot: #5b8fc2;
    --ink: #1e1e1e;
    --paper: #ffffff;
  }
  * { box-sizing: border-box; margin: 0; padding: 0; }
  html, body { width: 1200px; height: 848px; overflow: hidden; background: var(--paper); }
  .handout {
    position: relative; width: 1200px; height: 848px; overflow: hidden;
    font-family: "Barlow", Arial, sans-serif; color: var(--ink); font-size: 13.5px;
  }
  .backdrop {
    position: absolute; inset: 0;
    background:
      radial-gradient(ellipse 420px 260px at 720px 420px, rgba(120,160,200,.35), transparent 70%),
      radial-gradient(ellipse 500px 220px at 500px 120px, rgba(215,200,195,.35), transparent 70%),
      radial-gradient(ellipse 360px 200px at 1000px 250px, rgba(200,210,225,.35), transparent 70%),
      linear-gradient(180deg, #f6f8fb 0%, #e9eef4 60%, #f3f5f8 100%);
  }
  .waves { position: absolute; left: 0; top: 0; width: 1200px; height: 848px; }
  .title {
    position: absolute; left: 52px; top: 48px;
    font-family: "Archivo Black", Arial, sans-serif; font-size: 25px; letter-spacing: .2px; color: #111;
  }
  .tip { position: absolute; }
  .tip--left { left: 52px; width: 520px; }
  .tip--right { left: 660px; width: 500px; }
  .tip h2 {
    font-family: "Barlow Semi Condensed", Arial, sans-serif; font-weight: 700;
    font-size: 17px; color: var(--coral); line-height: 20px; margin-bottom: 6px;
  }
  .tip ul { list-style: none; }
  .tip li { position: relative; line-height: 17.4px; padding-left: 48px; }
  .tip li::before {
    content: ""; position: absolute; left: 25px; top: 6px;
    width: 5px; height: 5px; border-radius: 50%; background: var(--dot);
  }
  .tip li.gap { margin-top: 12px; }
  .tip li.strong { font-weight: 700; font-style: italic; }
  .tip li.sub { padding-left: 68px; color: var(--blue-text); margin-top: 5px; }
  .tip li.sub::before {
    content: "◊"; width: auto; height: auto; background: none; border-radius: 0;
    left: 36px; top: 0; color: var(--dot); font-size: 14px;
  }
  .closing {
    position: absolute; left: 40px; top: 728px; width: 520px; text-align: center;
    font-size: 22px; line-height: 29px; color: #111;
  }
  .closing strong { font-weight: 600; }
  .offer { position: absolute; left: 722px; top: 712px; color: #fff; }
  .offer-headline { font-weight: 700; font-size: 21px; }
  .offer-link { font-size: 13px; margin-top: 11px; }
  .offer-link b { font-weight: 700; }
</style>
</head>
<body>
<main class="handout">
  <div class="backdrop" role="img" aria-label="Soft faded photograph of a stethoscope resting on a clipboard"></div>

  <svg class="waves" viewBox="0 0 1200 848" aria-hidden="true">
    <path d="M0 574 C 200 610, 420 700, 640 702 C 860 704, 1030 610, 1200 568 L1200 848 L0 848 Z" fill="var(--coral)"/>
    <path d="M0 622 C 200 660, 380 712, 560 706 C 760 700, 980 640, 1200 596 L1200 848 L0 848 Z" fill="var(--blue-band)"/>
  </svg>

  <h1 class="title">11 Nursing Test Taking Tips</h1>

  <section class="tip tip--left" style="top:92px">
    <h2>SATA</h2>
    <ul><li>Evaluate each option individuals</li><li>Rearrange as a True/False Question</li></ul>
  </section>
  <section class="tip tip--left" style="top:172px">
    <h2>Absolute Words</h2>
    <ul><li>Always, Never, None, All, Every</li><li>RED FLAGS</li><li>May be correct if it's a safety issue</li></ul>
  </section>
  <section class="tip tip--left" style="top:264px">
    <h2>Opposites</h2>
    <ul><li>Two opposite answer choices usually means one is correct</li><li>Review before other options</li><li>Hyper vs Hypo, Acute vs Chronic, Overload vs Deficit</li></ul>
  </section>
  <section class="tip tip--left" style="top:356px">
    <h2>Same</h2>
    <ul><li style="width:400px">Answer options with the same concept means both are usually incorrect</li></ul>
  </section>
  <section class="tip tip--left" style="top:418px">
    <h2>Priority</h2>
    <ul>
      <li>ABCs, Pain, Education, Feelings</li>
      <li>Which option is closest to Airway</li>
      <li class="strong">ABCs</li>
      <li class="sub">Airway: NPO. gag reflex, breathing, airway</li>
      <li class="sub">Breathing: breath sounds, O2 admin, pulse ox, raise HOB</li>
      <li class="sub">Circulation: HR, BP, CPR, fluid status, diarrhea,<br>IV fluids, central lines, bleeding</li>
      <li class="sub">Safety: physical (rugs, nightlight, phone, falls) infection (assessing,<br>temp, hand washing, cultures, antibiotics, wounds)</li>
      <li style="margin-top:5px">Keywords: priority, emergency, ambulance, returning to floor, see first</li>
    </ul>
  </section>

  <section class="tip tip--right" style="top:50px">
    <h2>Nursing Process</h2>
    <ul><li>Always follow ADPIE</li></ul>
  </section>
  <section class="tip tip--right" style="top:108px">
    <h2>Acute vs Chronic</h2>
    <ul>
      <li>Content is KING</li>
      <li style="padding-left:48px;text-indent:0">If the question is asking about ACUTE condition, one of the options will<br><span style="margin-left:-48px">be about CHRONIC</span></li>
      <li class="gap">Acute vs Chronic, Short Term vs Long Term, Early Signs vs Late Signs</li>
    </ul>
  </section>
  <section class="tip tip--right" style="top:216px">
    <h2>What do they want to know?</h2>
    <ul><li>Read every word of the question</li><li>Remove distractors</li><li>Don't overthink</li><li class="gap">Correct or Incorrect Answer (except/further teaching)</li></ul>
  </section>
  <section class="tip tip--right" style="top:326px">
    <h2>Expected Findings vs Complications</h2>
    <ul><li>Rule out expected findings</li></ul>
  </section>
  <section class="tip tip--right" style="top:380px">
    <h2>Repeating Words</h2>
    <ul><li>Last ditch effort, when all else fails</li><li>Look for repeating words in question and answer options</li></ul>
  </section>
  <section class="tip tip--right" style="top:451px">
    <h2>RNX Question Traps</h2>
    <ul><li>No Assessment</li><li>Incomplete Assessment</li><li>Incorrect Assessment</li><li>“First” doesn't always mean assessment</li><li>“Action” doesn't always mean implementation</li><li>Determine the outcome of each answer option</li></ul>
  </section>

  <p class="closing">Use this guide to work through tests.<br><strong>Remember CONTENT is king.&nbsp; Learn all you can.</strong></p>

  <div class="offer">
    <p class="offer-headline">Save $75 on CAREWISE Academy while available.</p>
    <p class="offer-link"><b>Visit carewise.com/ace</b>&nbsp; ©2017 carewise.com</p>
  </div>
</main>
</body>
</html>
```